CrestHornSupply.com

I need a new webdesign for a company in the San Jose/SF Bay area that showcases the financial benefits of buying used band instruments for junior high students.This would be opposed to the current and costly option of renting cheap quality instruments from the 2 or 3 local music stores that charge a monthly fee that over the years charges the buyer 3 or 4x over..
Instruments: focus in on Alto Sax, Trumpet, Flute, Clarinet, Trombone, Tenor Sax, Baritone
Target middle schools are Willowmere Middle School and Harlan Middle School in San Jose, CA. Both have award winning band programs.
Files attached may or may not be important.
Tabs Needed and funtional
Contact
Shopping Cart
Select Instrument
Checkout
Add to Cart, etc.
Instuments
quantity, etc.
trade in your instrument/sell your instrument
ability to add or take away new instruments for sale. including pictures
Additional questions or info, feel free to ask
Updates
Hi Designers,
Project Deadline Extended
Reason: In the next week you will be receiving specific content that will be required to be had on the website.
New desigins are still welcome. Please continue to contact me if you have questions about your individual designs.
Thanks!
Crest Horn

```html
<!DOCTYPE html>
<html lang="en">
<head>
<meta charset="utf-8">
<title>CrestHornSupply.com</title>
<link rel="stylesheet" href="https://fonts.googleapis.com/css2?family=Open+Sans:ital,wght@0,400;0,600;0,700;1,400&family=Cinzel:wght@700&display=swap">
<style>
:root{
  --bg-dark:#2a2b2e;
  --bg-mid:#3b3c40;
  --nav:#2e2f33;
  --red:#93001f;
  --green:#2a6a3d;
  --black:#111112;
  --gold:#8c6a2f;
  --gold-text:#f3c33b;
  --text:#ffffff;
  --muted:#d6d6d6;
  --footer:#141414;
  --price:#1f7a3a;
}
*{box-sizing:border-box;margin:0;padding:0}
html,body{width:1200px;height:1067px;overflow:hidden}
body{font-family:"Open Sans",Arial,sans-serif;color:var(--text);position:relative;background:var(--bg-dark)}
.backdrop{position:absolute;inset:0;background:
  radial-gradient(ellipse at 60% 20%,#55565a 0%,transparent 55%),
  radial-gradient(ellipse at 75% 80%,#5a3f22 0%,transparent 50%),
  linear-gradient(180deg,#46474b 0%,#2f3033 45%,#3a2d22 80%,#1c1a18 100%)}
.site-header{position:absolute;left:0;top:0;width:1200px;height:104px}
.logo{position:absolute;left:76px;top:38px;display:flex;align-items:center;gap:10px;font-weight:700;font-size:27px;color:var(--gold-text);letter-spacing:.3px}
.logo-mark{width:18px;height:18px;background:var(--gold-text)}
.account-links{position:absolute;right:76px;top:22px;font-size:18px;color:var(--muted)}
.account-links a{color:var(--muted);text-decoration:none}
.account-links a.active{color:var(--gold-text)}
.account-links .sep{margin:0 8px;color:#8a8a8a}
.cart{position:absolute;left:945px;top:50px;display:flex;gap:14px}
.cart-title{color:var(--gold-text);font-weight:700;font-size:18px;line-height:1.2}
.cart-sum{font-size:15px;color:var(--muted)}
.main-nav{position:absolute;left:0;top:104px;width:1200px;height:58px;background:var(--nav);border-top:1px solid #555;border-bottom:1px solid #555}
.main-nav ul{list-style:none;display:flex;position:absolute;left:78px;top:0;height:58px}
.main-nav li{padding:0 20px;line-height:56px;font-weight:600;font-size:18px;border-right:1px solid #444}
.main-nav li.current{background:var(--red)}
.search{position:absolute;left:885px;top:12px;display:flex}
.search-field{width:208px;height:35px;background:#fff}
.search-btn{width:34px;height:35px;background:var(--red);display:flex;align-items:center;justify-content:center}
.slider{position:absolute;left:66px;top:186px;width:660px;height:435px;border:2px solid #222;box-shadow:0 0 6px rgba(0,0,0,.6)}
.slider-photo{position:absolute;inset:0;background:radial-gradient(ellipse at 70% 25%,#9a2410 0%,#3b0c06 35%,transparent 60%),linear-gradient(160deg,#1b1211 0%,#5a5a5c 55%,#c9c9cb 75%,#2b2b2b 100%)}
.slider-caption{position:absolute;left:0;bottom:0;width:100%;height:67px;background:rgba(10,10,12,.85);display:flex;align-items:center;justify-content:space-between;padding:0 16px}
.slider-caption p{font-style:italic;font-size:24px}
.btn-buy{background:var(--red);font-weight:600;font-size:16px;padding:6px 11px;border:1px solid #c33}
.promo{position:absolute;left:742px;width:391px;height:97px;text-align:center;box-shadow:0 0 6px rgba(0,0,0,.6);border:2px solid rgba(255,255,255,.08)}
.promo h2{font-family:"Cinzel",Georgia,serif;font-size:32px;line-height:1;margin-top:10px;letter-spacing:.5px}
.promo h2 small{font-size:22px}
.promo p{font-size:17px;line-height:22px}
.promo-shipping{top:189px;background:var(--red)}
.promo-sale{top:301px;background:var(--green)}
.promo-news{top:413px;background:var(--black)}
.promo-updates{top:525px;background:var(--gold)}
.section-title{position:absolute;left:57px;top:648px;font-size:26px;font-weight:600}
.section-rule{position:absolute;left:240px;top:673px;width:855px;height:2px;background:linear-gradient(90deg,#6a6a6a,#444)}
.section-tab{position:absolute;left:1095px;top:644px;width:49px;height:30px;background:#4a2f25;clip-path:polygon(30% 0,70% 0,100% 100%,0 100%);display:flex;align-items:center;justify-content:center}
.product{position:absolute;top:698px;width:253px;height:241px;box-shadow:0 0 6px rgba(0,0,0,.7);border:1px solid #333}
.product-photo{position:absolute;left:0;top:0;width:100%;height:207px}
.product-name{position:absolute;left:0;bottom:0;width:100%;height:34px;background:var(--gold);text-align:center;line-height:34px;font-size:14px}
.product-active{left:56px;background:var(--red);text-align:center}
.product-actions{display:flex;justify-content:center;gap:12px;margin-top:45px}
.product-actions span{width:45px;height:40px;background:var(--gold);display:flex;align-items:center;justify-content:center}
.product-active .product-name-plain{margin-top:35px;font-size:14px}
.price{display:inline-block;margin-top:32px;background:var(--price);font-weight:600;font-size:16px;padding:2px 8px;border:1px solid #ddd}
.p2{left:334px}.p3{left:613px}.p4{left:891px}
.p2 .product-photo{background:radial-gradient(circle at 50% 45%,#b5832c 0%,#3a2a12 40%,#100c08 75%)}
.p3 .product-photo{background:radial-gradient(circle at 50% 50%,#8a3a12 0%,#33180b 40%,#100c08 75%)}
.p4 .product-photo{background:radial-gradient(circle at 50% 45%,#c89a3a 0%,#3a2a12 40%,#100c08 75%)}
.site-footer{position:absolute;left:0;top:981px;width:1200px;height:86px;background:var(--footer)}
.footer-links{position:absolute;left:54px;top:17px;font-size:15px}
.footer-links a{color:#eee;text-decoration:none}
.footer-links a.active{color:#d23a3a}
.footer-links .sep{margin:0 6px}
.copyright{position:absolute;left:54px;top:49px;font-size:15px}
.payments{position:absolute;left:881px;top:19px;display:flex;gap:8px}
.payments span{width:55px;height:35px;border-radius:3px}
.pay-1{background:#f4f4f4}.pay-2{background:#f1e6c8}.pay-3{background:#1c3f8f}.pay-4{background:#f5d92a}
</style>
</head>
<body>
<div class="backdrop" role="img" aria-label="Blurred photo of brass and string instruments on a dark stage"></div>

<header class="site-header">
  <div class="logo"><span class="logo-mark"></span>CrestHornSupply.com</div>
  <nav class="account-links">
    <a class="active" href="#">My Account</a><span class="sep">/</span><a href="#">My Wishlist</a><span class="sep">/</span><a href="#">Checkout</a><span class="sep">/</span><a href="#">Log In</a>
  </nav>
  <div class="cart">
    <svg width="48" height="50" viewBox="0 0 48 50" aria-hidden="true"><path d="M4 14h40l-3 34H7z" fill="#f2f2f2"/><path d="M16 16V9a8 8 0 0 1 16 0v7" fill="none" stroke="#c22" stroke-width="2"/></svg>
    <div><div class="cart-title">My Cart:</div><div class="cart-sum">0 item(s) - $0.00</div></div>
  </div>
</header>

<nav class="main-nav">
  <ul>
    <li class="current">Home</li><li>About</li><li>Who we are</li><li>Shop</li><li>Instuments</li><li>Locations</li><li>Contact</li>
  </ul>
  <div class="search">
    <div class="search-field"></div>
    <div class="search-btn"><svg width="18" height="18" viewBox="0 0 18 18" aria-hidden="true"><circle cx="7" cy="7" r="5" fill="none" stroke="#fff" stroke-width="2.5"/><path d="M11 11l5 5" stroke="#fff" stroke-width="3"/></svg></div>
  </div>
</nav>

<section class="slider">
  <div class="slider-photo" role="img" aria-label="Violin resting on a silver saxophone"></div>
  <div class="slider-caption"><p>Lorem ipsum dolor sit consectetur adipiscing.</p><span class="btn-buy">Phrchase&nbsp; Now</span></div>
</section>

<aside>
  <div class="promo promo-shipping"><h2>FREE SHIPPING</h2><p>ON ORDERS OVER $499<br>This offer is valid all our store items</p></div>
  <div class="promo promo-sale"><h2>SALE <small>UP TO</small> 70%</h2><p>ON ORDERS OVER $499<br>This offer is valid all our store items</p></div>
  <div class="promo promo-news"><h2>OUR NEWSLETTER</h2><p>ON ORDERS OVER $499<br>This offer is valid all our store items</p></div>
  <div class="promo promo-updates"><h2>LATEST UPDATES</h2><p>ON ORDERS OVER $499<br>This offer is valid all our store items</p></div>
</aside>

<h2 class="section-title">NEW Products</h2>
<div class="section-rule"></div>
<div class="section-tab"><svg width="18" height="18" viewBox="0 0 18 18" aria-hidden="true"><g fill="none" stroke="#fff" stroke-width="2.2"><rect x="2" y="7" width="8" height="5" rx="2.5" transform="rotate(-45 6 9.5)"/><rect x="8" y="6" width="8" height="5" rx="2.5" transform="rotate(-45 12 8.5)"/></g></svg></div>

<article class="product product-active">
  <div class="product-actions">
    <span><svg width="24" height="24" viewBox="0 0 24 24" aria-hidden="true"><g fill="none" stroke="#fff" stroke-width="2.6"><rect x="2" y="10" width="11" height="6" rx="3" transform="rotate(-45 7.5 13)"/><rect x="11" y="8" width="11" height="6" rx="3" transform="rotate(-45 16.5 11)"/></g></svg></span>
    <span><svg width="26" height="24" viewBox="0 0 26 24" aria-hidden="true"><path d="M1 3h4l3 12h13l3-9H7" fill="none" stroke="#fff" stroke-width="2.2"/><circle cx="10" cy="20" r="2" fill="#fff"/><circle cx="19" cy="20" r="2" fill="#fff"/></svg></span>
    <span><svg width="24" height="24" viewBox="0 0 24 24" aria-hidden="true"><circle cx="10" cy="10" r="7" fill="none" stroke="#fff" stroke-width="2.6"/><path d="M15 15l7 7M7 10h6M10 7v6" stroke="#fff" stroke-width="2.6"/></svg></span>
  </div>
  <p class="product-name-plain">Lorem Ispum daolar sit lorem</p>
  <span class="price">$499.00</span>
</article>
<article class="product p2"><div class="product-photo" role="img" aria-label="Gold alto saxophone"></div><div class="product-name">Lorem Ispum daolar sit lorem</div></article>
<article class="product p3"><div class="product-photo" role="img" aria-label="Violin with bow"></div><div class="product-name">Lorem Ispum daolar sit lorem</div></article>
<article class="product p4"><div class="product-photo" role="img" aria-label="Brass baritone horn"></div><div class="product-name">Lorem Ispum daolar sit lorem</div></article>

<footer class="site-footer">
  <nav class="footer-links">
    <a class="active" href="#">Home</a><span class="sep">/</span><a href="#">Shop</a><span class="sep">/</span><a href="#">Directory</a><span class="sep">/</span><a href="#">Members</a><span class="sep">/</span><a href="#">Blog</a><span class="sep">/</span><a href="#">Recommended</a><span class="sep">/</span><a href="#">Contacts</a>
  </nav>
  <p class="copyright">Copyright © 2014 Northgate Studio All Rights Reserved.</p>
  <div class="payments" aria-label="Accepted payment methods">
    <span class="pay-1"></span><span class="pay-2"></span><span class="pay-3"></span><span class="pay-4"></span>
  </div>
</footer>
</body>
</html>
```